M Zyvantics Buisness Cards

I need a technology focused clean business card for my employees. I have attached out logo to include in the mocks. We're a modern tech consulting firm that drives to interface humanity with technology in a truly cohesive fashion.

```html
<!DOCTYPE html>
<html lang="en">
<head>
<meta charset="utf-8">
<title>M Zyvantics Business Cards</title>
<link rel="stylesheet" href="https://fonts.googleapis.com/css2?family=Roboto+Condensed:wght@400;700&family=Roboto:wght@400;500&display=swap">
<style>
  :root {
    --page-bg: #2b2b2d;
    --card-bg: #1f1f21;
    --brand-blue: #1e8ad6;
    --text-light: #f2f2f2;
    --text-grey: #8f8f93;
    --logo-grey: #c9c9cc;
    --divider: #6b6b6f;
  }
  * { box-sizing: border-box; margin: 0; padding: 0; }
  html, body {
    width: 1200px; height: 900px; overflow: hidden;
    background: var(--page-bg);
  }
  .canvas {
    position: relative; width: 1200px; height: 900px;
    display: flex; flex-direction: column; align-items: center; justify-content: center; gap: 40px;
  }
  .card {
    position: relative; width: 700px; height: 400px;
    background: var(--card-bg);
    box-shadow: 0 10px 30px rgba(0,0,0,0.45);
  }
  /* Front */
  .card-front { display: flex; flex-direction: column; align-items: center; justify-content: center; }
  .brand { display: flex; align-items: center; gap: 18px; margin-top: 10px; }
  .brand-dot { width: 34px; height: 34px; border-radius: 50%; background: var(--brand-blue); }
  .brand-name {
    font-family: "Roboto Condensed", sans-serif; font-weight: 700;
    font-size: 58px; letter-spacing: 2px; color: var(--logo-grey);
  }
  .front-url {
    margin-top: 56px;
    font-family: "Roboto", sans-serif; font-size: 15px; letter-spacing: 8px;
    color: var(--text-light);
  }
  /* Back */
  .identity {
    position: absolute; right: 390px; top: 118px; text-align: right;
  }
  .person-name {
    font-family: "Roboto Condensed", sans-serif; font-weight: 700;
    font-size: 36px; color: var(--brand-blue); line-height: 1;
  }
  .person-role {
    font-family: "Roboto Condensed", sans-serif; font-size: 19px;
    color: var(--text-grey); margin-top: 4px; letter-spacing: 0.5px;
  }
  .divider {
    position: absolute; left: 333px; top: 100px; width: 2px; height: 110px;
    background: linear-gradient(var(--card-bg), var(--divider), var(--card-bg));
  }
  .contacts { position: absolute; left: 355px; top: 100px; list-style: none; }
  .contacts li {
    display: flex; align-items: center; gap: 10px; height: 22px;
    font-family: "Roboto", sans-serif; font-weight: 500; font-size: 17px; color: var(--text-light);
  }
  .contacts svg { width: 15px; height: 15px; fill: var(--brand-blue); flex: none; }
  .address {
    position: absolute; left: 160px; bottom: 110px;
    display: flex; align-items: center; gap: 6px;
    font-family: "Roboto", sans-serif; font-weight: 500; font-size: 18px; color: var(--text-light);
  }
  .address svg { width: 15px; height: 20px; fill: var(--brand-blue); }
</style>
</head>
<body>
<main class="canvas">
  <section class="card card-front">
    <div class="brand">
      <span class="brand-dot"></span>
      <span class="brand-name">M Zyvantics</span>
    </div>
    <p class="front-url">www.mzyvantics.com</p>
  </section>

  <section class="card card-back">
    <div class="identity">
      <h1 class="person-name">DANIEL HART</h1>
      <p class="person-role">CEO/FOUNDER</p>
    </div>
    <div class="divider"></div>
    <ul class="contacts">
      <li><svg viewBox="0 0 24 24"><path d="M6.6 10.8a15 15 0 0 0 6.6 6.6l2.2-2.2c.3-.3.7-.4 1-.2 1.1.4 2.3.6 3.6.6.6 0 1 .4 1 1V20c0 .6-.4 1-1 1A17 17 0 0 1 3 4c0-.6.4-1 1-1h3.5c.6 0 1 .4 1 1 0 1.3.2 2.5.6 3.6.1.3 0 .7-.2 1z"/></svg>555 210 3481</li>
      <li><svg viewBox="0 0 24 24"><path d="M7 1h10a2 2 0 0 1 2 2v18a2 2 0 0 1-2 2H7a2 2 0 0 1-2-2V3a2 2 0 0 1 2-2zm0 3v15h10V4zm5 16.2a1 1 0 1 0 0 2 1 1 0 0 0 0-2z"/></svg>555 872 6140</li>
      <li><svg viewBox="0 0 24 24"><path d="M6 2h12v5H6zM4 8h16a2 2 0 0 1 2 2v7h-4v5H6v-5H2v-7a2 2 0 0 1 2-2zm4 8v4h8v-4z"/></svg>555 394 7205</li>
      <li><svg viewBox="0 0 24 24"><path d="M2 5h20v14H2zm2 2v.5l8 5 8-5V7zm0 2.9V17h16V9.9l-8 5z"/></svg>daniel@mzyvantics.com</li>
      <li><svg viewBox="0 0 24 24"><path d="M12 2a10 10 0 1 0 0 20 10 10 0 0 0 0-20zm-1 17.9A8 8 0 0 1 4.2 10.5L9 15v1a2 2 0 0 0 2 2zm6.9-2.5A2 2 0 0 0 16 16h-1v-3a1 1 0 0 0-1-1H8v-2h2a1 1 0 0 0 1-1V7h2a2 2 0 0 0 2-2v-.4a8 8 0 0 1 2.9 12.8z"/></svg>www.mzyvantics.com</li>
    </ul>
    <p class="address"><svg viewBox="0 0 24 32"><path d="M12 0A12 12 0 0 0 0 12c0 9 12 20 12 20s12-11 12-20A12 12 0 0 0 12 0zm0 17a5 5 0 1 1 0-10 5 5 0 0 1 0 10z"/></svg>4120 Larkspur Way, Juneau, Alaska 99801</p>
  </section>
</main>
</body>
</html>
```